Harbourline Refrigeration business card design

We would like a new design for our business card as we have a new logo.
We need generic business card to give our customers with our office details - with the option of making it individualized for each manager

Target Market(s)

Companies and homeowners

Industry/Entity Type

Air Conditioning

Contact Information for Business Card

We are not sure if we want single or double sided it will depend on the design we choose

Colors
33a6d7
0255a3

Requirements
Must have
• Logo
• phone: (08) 8721 5940
• email: harbourserve@tealnet.example
• website: www.harbourlinerefrigeration.example
• AU61420
• BLD472913
Nice to have
• Address - Shed 5/284 Tallis Rd, Whyalla Norrie SA 5608

```html
<!DOCTYPE html>
<html lang="en">
<head>
<meta charset="UTF-8">
<title>Harbourline Refrigeration – Business Card</title>
<link rel="stylesheet" href="https://fonts.googleapis.com/css2?family=Montserrat:wght@400;500;600;700;800&display=swap">
<style>
  :root {
    --navy: #154a86;
    --navy-deep: #0f3d74;
    --brand-blue: #0255a3;
    --mid-blue: #2a8fd0;
    --sky-blue: #33a6d7;
    --pale-blue: #8fcdea;
    --ink: #3c3c3c;
    --ink-soft: #555;
    --paper: #ffffff;
    --stage: #eceef1;
  }
  * { box-sizing: border-box; margin: 0; padding: 0; }
  html, body { width: 1200px; height: 960px; overflow: hidden; }
  body {
    background: var(--stage);
    font-family: "Montserrat", sans-serif;
    display: flex;
    flex-direction: column;
    align-items: center;
    justify-content: center;
    gap: 36px;
  }
  .card {
    position: relative;
    width: 700px;
    height: 420px;
    border-radius: 6px;
    overflow: hidden;
    box-shadow: 0 6px 18px rgba(0,0,0,0.15);
  }

  /* Back side */
  .card-back {
    background: var(--navy);
    color: var(--paper);
  }
  .card-back .map-area {
    position: absolute;
    left: 70px; top: 40px;
    width: 560px; height: 250px;
    border-radius: 40px;
    background: radial-gradient(ellipse at center, rgba(255,255,255,0.09), rgba(255,255,255,0) 70%);
  }
  .card-back .brand {
    position: absolute;
    top: 130px; left: 0; right: 0;
    display: flex; align-items: center; justify-content: center; gap: 16px;
  }
  .card-back .brand-dot {
    width: 22px; height: 22px; border-radius: 50%;
    background: var(--sky-blue);
  }
  .card-back .brand-name {
    font-weight: 700;
    font-size: 40px;
    letter-spacing: 0.5px;
    color: var(--paper);
  }
  .card-back .office {
    position: absolute;
    top: 250px; left: 0; right: 0;
    text-align: center;
    font-size: 17px;
    font-weight: 500;
    line-height: 1.7;
  }

  /* Front side */
  .card-front { background: var(--paper); }
  .card-front .brand {
    position: absolute;
    left: 40px; top: 122px;
    width: 230px;
    display: flex; align-items: center; gap: 10px;
  }
  .card-front .brand-dot {
    flex: none;
    width: 16px; height: 16px; border-radius: 50%;
    background: var(--sky-blue);
  }
  .card-front .brand-name {
    font-weight: 700;
    font-size: 25px;
    line-height: 1.15;
    color: var(--brand-blue);
  }
  .card-front .divider {
    position: absolute;
    left: 292px; top: 80px;
    width: 1px; height: 180px;
    background: #9a9a9a;
  }
  .card-front .person {
    position: absolute;
    left: 322px; top: 80px;
    right: 24px;
  }
  .person-name {
    font-weight: 800;
    font-size: 30px;
    color: var(--ink);
    white-space: nowrap;
  }
  .person-role {
    font-size: 16px;
    color: var(--ink-soft);
    margin-top: 2px;
  }
  .contact-list {
    list-style: none;
    margin-top: 30px;
    font-size: 15px;
    color: var(--ink);
  }
  .contact-list li {
    display: flex; align-items: center; gap: 10px;
    height: 27px;
    white-space: nowrap;
  }
  .contact-list svg { width: 17px; height: 17px; flex: none; }
  .card-front .waves {
    position: absolute; left: 0; bottom: 0;
    width: 700px; height: 140px;
  }
  .card-front .licences {
    position: absolute;
    left: 34px; bottom: 38px;
    color: var(--paper);
    font-weight: 600;
    font-size: 18px;
    letter-spacing: 0.3px;
  }
</style>
</head>
<body>

  <section class="card card-back" aria-label="Business card back">
    <div class="map-area" role="img" aria-label="Faint dotted world map"></div>
    <div class="brand">
      <span class="brand-dot"></span>
      <span class="brand-name">Harbourline Refrigeration</span>
    </div>
    <div class="office">
      <p>Shed 5/284 Tallis Rd, Whyalla Norrie SA 5608</p>
      <p>www.harbourlinerefrigeration.example</p>
    </div>
  </section>

  <section class="card card-front" aria-label="Business card front">
    <div class="brand">
      <span class="brand-dot"></span>
      <span class="brand-name">Harbourline Refrigeration</span>
    </div>
    <div class="divider"></div>
    <div class="person">
      <p class="person-name">Daniel BROOKS</p>
      <p class="person-role">Managing Director</p>
      <ul class="contact-list">
        <li>
          <svg viewBox="0 0 24 24" fill="var(--brand-blue)"><path d="M6.6 10.8a15 15 0 0 0 6.6 6.6l2.2-2.2c.3-.3.7-.4 1-.2 1.1.4 2.3.6 3.6.6.6 0 1 .4 1 1V20c0 .6-.4 1-1 1A17 17 0 0 1 3 4c0-.6.4-1 1-1h3.5c.6 0 1 .4 1 1 0 1.2.2 2.4.6 3.6.1.3 0 .7-.2 1z"/></svg>
          (08) 8721 5940
        </li>
        <li>
          <svg viewBox="0 0 24 24" fill="none" stroke="var(--brand-blue)" stroke-width="1.6"><rect x="3" y="6" width="18" height="12"/><path d="M3 6l9 7 9-7"/></svg>
          harbourserve@tealnet.example
        </li>
        <li>
          <svg viewBox="0 0 24 24" fill="none" stroke="var(--brand-blue)" stroke-width="1.6"><circle cx="12" cy="12" r="9"/><path d="M3 12h18M12 3c3 3 3 15 0 18M12 3c-3 3-3 15 0 18"/></svg>
          www.harbourlinerefrigeration.example
        </li>
      </ul>
    </div>
    <svg class="waves" viewBox="0 0 700 140" preserveAspectRatio="none" aria-hidden="true">
      <path d="M0 50 C140 0 300 20 420 80 C520 125 620 120 700 110 L700 140 L0 140 Z" fill="var(--pale-blue)"/>
      <path d="M0 52 C130 10 270 30 380 90 C470 135 600 140 700 122 L700 140 L0 140 Z" fill="var(--mid-blue)"/>
      <path d="M0 60 C120 25 240 45 330 100 C400 140 560 150 700 128 L700 140 L0 140 Z" fill="var(--navy-deep)"/>
      <path d="M450 95 C540 112 620 110 700 98 L700 102 C620 114 540 116 450 99 Z" fill="var(--navy-deep)"/>
    </svg>
    <p class="licences">AU61420 • BLD472913</p>
  </section>

</body>
</html>
```